"Pause. Pivot. Prosper." Empowerment Book Cover

Hello, I need a hot, trendy, and contemporary book cover designed for my first book called "Pause. Pivot. Prosper. -- 365 Bold Confidence Notes for Anyone Seeking to Pause, Pivot, and Prosper Across Career & Personal Dreams."
This is my first book and I am really wanting to launch my brand with it... it would be awesome to match the inside/outside branding of the book. So we can either create the book cover to match the book guts, or update the book guts to match the cover.
Lastly, I just got a professional photoshoot done last week so we can use one of those images, or we can go with a different idea/style for the cover. The body of the book is attached. All questions welcomed, happy designing!
Target Market(s)
Gen Z, Millennials and Gen X.
Industry/Entity Type
Personal Development.
Requirements
Must have
- It must stand out and be different from other typical book covers.
Nice to have
- Success, Inspiration, Motivation, Mindset, Growth.
Should not have
- Clipart, stock art, stock look and feel.

```html
<!DOCTYPE html>
<html lang="en">
<head>
<meta charset="utf-8">
<title>Pause. Pivot. Prosper. — Book Cover</title>
<link rel="stylesheet" href="https://fonts.googleapis.com/css2?family=Questrial&display=swap">
<style>
  :root {
    --page-bg: #ffffff;
    --cover-bg: #e1e1e1;
    --title-blue: #1456b4;
    --author-white: #ffffff;
    --portrait-light: #d2d2d2;
    --portrait-mid: #8a8a8a;
    --portrait-dark: #2b2b2b;
  }
  * { box-sizing: border-box; margin: 0; padding: 0; }
  html, body {
    width: 1200px;
    height: 895px;
    overflow: hidden;
    background: var(--page-bg);
  }
  .canvas {
    position: relative;
    width: 1200px;
    height: 895px;
  }
  .book-cover {
    position: absolute;
    left: 315px;
    top: 20px;
    width: 570px;
    height: 855px;
    background: var(--cover-bg);
    overflow: hidden;
    font-family: "Questrial", "Century Gothic", sans-serif;
    box-shadow: 0 6px 24px rgba(0, 0, 0, 0.18);
  }
  .author-portrait {
    position: absolute;
    left: 0;
    top: 0;
    width: 570px;
    height: 855px;
  }
  .book-title {
    position: absolute;
    left: 40px;
    top: 52px;
    color: var(--title-blue);
    font-weight: 400;
    font-size: 98px;
    line-height: 0.94;
    letter-spacing: 1px;
  }
  .book-title span { display: block; }
  .book-subtitle {
    position: absolute;
    left: 38px;
    top: 448px;
    color: var(--title-blue);
    font-size: 19px;
    line-height: 1.22;
  }
  .book-subtitle .lead {
    display: block;
    font-size: 24px;
    line-height: 1.15;
    letter-spacing: -0.3px;
  }
  .book-subtitle .rest { display: block; }
  .author-name {
    position: absolute;
    left: 140px;
    top: 748px;
    color: var(--author-white);
    font-size: 34px;
    letter-spacing: 0.3px;
  }
</style>
</head>
<body>
<main class="canvas">
  <section class="book-cover">
    <svg class="author-portrait" viewBox="0 0 570 855" role="img" aria-label="Black-and-white portrait photograph of the author in a dark suit and white shirt, smiling and looking to the side">
      <defs>
        <linearGradient id="portrait-tone" x1="0" y1="0" x2="0" y2="1">
          <stop offset="0" stop-color="var(--portrait-light)" stop-opacity="0"/>
          <stop offset="0.35" stop-color="var(--portrait-mid)" stop-opacity="0.55"/>
          <stop offset="0.7" stop-color="var(--portrait-dark)" stop-opacity="0.9"/>
          <stop offset="1" stop-color="var(--portrait-dark)"/>
        </linearGradient>
        <linearGradient id="portrait-fade" x1="0" y1="0" x2="1" y2="0">
          <stop offset="0" stop-color="#fff" stop-opacity="0"/>
          <stop offset="0.35" stop-color="#fff" stop-opacity="1"/>
        </linearGradient>
        <mask id="portrait-mask">
          <rect x="0" y="0" width="570" height="855" fill="url(#portrait-fade)"/>
        </mask>
      </defs>
      <path d="M300 300 Q420 250 540 300 L570 330 L570 855 L70 855 Q120 720 200 640 Q260 600 300 560 Z"
            fill="url(#portrait-tone)" mask="url(#portrait-mask)"/>
    </svg>

    <h1 class="book-title">
      <span>Pause.</span>
      <span>Pivot.</span>
      <span>Prosper.</span>
    </h1>

    <p class="book-subtitle">
      <span class="lead">365 Bold</span>
      <span class="lead">Confidence Notes</span>
      <span class="rest">for Anyone Seeking to</span>
      <span class="rest">Pause, Pivot, and Prosper</span>
      <span class="rest">Across Career &amp;</span>
      <span class="rest">Personal Dreams.</span>
    </p>

    <p class="author-name">Samir Qadri</p>
  </section>
</main>
</body>
</html>
```